Marvane Painting Epoxy Flyer

We need a promotional flyer for a new epoxy floor coatings division of our painting company. We do epoxy garage floor coatings and paver sealing. It needs to be based on and very similar to the attached flyer. The garage floor picture needs to look more realistic, and the before and after pavers pictures should look less shiny but still a good contrast. Include attached logo

```html
<!DOCTYPE html>
<html lang="en">
<head>
<meta charset="utf-8">
<title>Marvane Painting – Garage &amp; Driveway Flyer</title>
<link href="https://fonts.googleapis.com/css2?family=Oswald:wght@500;600;700&family=Poppins:wght@500;600;700&display=swap" rel="stylesheet">
<style>
  :root {
    --backdrop: #d3d3d3;
    --blue: #2488e2;
    --teal: #2e9c98;
    --green: #49a82a;
    --orange: #c0670c;
    --black: #000;
    --white: #fff;
    --ink: #111;
  }
  * { box-sizing: border-box; margin: 0; padding: 0; }
  html, body { width: 904px; height: 1200px; overflow: hidden; }
  body { background: var(--backdrop); position: relative; font-family: "Poppins", sans-serif; }

  .flyer {
    position: absolute; left: 137px; top: 127px; width: 630px; height: 946px;
    background: var(--white); overflow: hidden;
  }
  .hero-band {
    position: absolute; left: 0; top: 0; width: 630px; height: 596px;
    background: linear-gradient(180deg, var(--blue) 0%, var(--teal) 40%, var(--green) 75%, var(--green) 100%);
  }
  .dark-band { position: absolute; left: 0; top: 596px; width: 630px; height: 240px; background: var(--black); }
  .logo-blob { position: absolute; left: 0; top: 0; }

  .brand {
    position: absolute; left: 22px; top: 60px; display: flex; align-items: center; gap: 8px;
    font-family: "Poppins", sans-serif; font-weight: 600; font-size: 17px; color: var(--ink);
  }
  .brand-dot { width: 14px; height: 14px; border-radius: 50%; background: var(--teal); }

  .headline {
    position: absolute; left: 258px; top: 10px; width: 370px;
    font-family: "Oswald", sans-serif; font-weight: 700; color: var(--white);
    text-shadow: 0 2px 3px rgba(0,0,0,.25);
  }
  .headline .line-1 { display: block; font-size: 63px; line-height: 68px; letter-spacing: -0.5px; white-space: nowrap; }
  .headline .line-2 { display: block; font-size: 46px; line-height: 52px; letter-spacing: -0.5px; white-space: nowrap; }
  .subhead {
    position: absolute; left: 258px; top: 133px; white-space: nowrap;
    font-weight: 600; font-size: 21.3px; color: var(--white); letter-spacing: 0.2px;
  }

  .photo {
    position: absolute; width: 248px; border: 2px solid var(--black);
    border-radius: 16px 16px 0 0; overflow: hidden;
  }
  .photo.row-1 { top: 192px; height: 158px; }
  .photo.row-2 { top: 357px; height: 147px; }
  .photo.col-1 { left: 61px; }
  .photo.col-2 { left: 323px; }
  .garage-before { background: linear-gradient(180deg, #d9d5c8 0%, #c3c6c3 22%, #b4b8b6 60%, #c9cbc9 100%); }
  .garage-after  { background: linear-gradient(180deg, #e6e2d8 0%, #cfd0cc 25%, #e4e5e2 50%, #bdbfbc 100%); }
  .paver-before  { background: linear-gradient(180deg, #9b9888 0%, #5f7a3c 18%, #7d7167 35%, #6c625a 100%); }
  .paver-after   { background: linear-gradient(180deg, #8f9180 0%, #4e7d2c 18%, #3e3e40 36%, #2b2b2e 100%); }

  .tag {
    position: absolute; left: 0; top: 0; width: 36px; height: 98px;
    border-radius: 0 0 18px 0;
    display: flex; align-items: center; justify-content: center;
    font-family: "Oswald", sans-serif; font-weight: 700; font-size: 22px;
  }
  .tag span { writing-mode: vertical-rl; transform: rotate(180deg); }
  .tag.before { background: var(--black); color: var(--white); }
  .tag.after { background: var(--white); color: var(--black); }

  .services {
    position: absolute; left: 30px; top: 502px; width: 570px; height: 240px;
    background: var(--white); border: 2px solid var(--black); border-radius: 18px;
  }
  .service {
    position: absolute; top: 35px; width: 263px; height: 152px; border-radius: 12px;
    background: linear-gradient(180deg, var(--blue) 0%, var(--green) 50%, var(--orange) 100%);
  }
  .service.epoxy { left: 18px; }
  .service.sealing { left: 291px; }
  .service-title {
    position: absolute; left: 16px; top: -16px; width: 230px; height: 32px; border-radius: 16px;
    background: var(--black); color: var(--white); text-align: center;
    font-family: "Oswald", sans-serif; font-weight: 600; font-size: 22px; line-height: 32px;
  }
  .benefits { position: absolute; top: 28px; right: 4px; list-style: none; }
  .epoxy .benefits { left: 31px; }
  .sealing .benefits { left: 14px; }
  .benefits li {
    position: relative; padding-left: 17px; margin-bottom: 10px; white-space: nowrap;
    font-weight: 500; font-size: 13px; line-height: 16px; color: var(--white);
  }
  .benefits li svg { position: absolute; left: 0; top: 3px; }
  .tagline {
    position: absolute; left: 0; right: 0; top: 197px; text-align: center;
    font-family: "Oswald", sans-serif; font-weight: 600; font-size: 24px; letter-spacing: -0.4px; color: var(--ink);
  }

  .trust { position: absolute; top: 760px; display: flex; align-items: center; gap: 12px; }
  .trust.licensed { left: 45px; }
  .trust.family { left: 211px; }
  .trust.area { left: 398px; }
  .trust-icon { width: 48px; height: 48px; }
  .trust-text {
    font-family: "Oswald", sans-serif; font-weight: 500; font-size: 19.5px; line-height: 21px; color: var(--white);
  }

  .cta { position: absolute; left: 31px; top: 852px; font-family: "Oswald", sans-serif; font-weight: 700; color: var(--black); }
  .cta .small { display: block; font-size: 33px; line-height: 34px; letter-spacing: -0.5px; white-space: nowrap; transform: scaleX(0.87); transform-origin: left center; }
  .cta .big { display: block; font-size: 55px; line-height: 52px; letter-spacing: -0.5px; transform: scaleX(0.96); transform-origin: left center; }
  .phone-icon { position: absolute; left: 250px; top: 858px; }
  .phone-number {
    position: absolute; left: 296px; top: 857px; white-space: nowrap;
    font-weight: 700; font-size: 40.5px; line-height: 44px; color: var(--black); letter-spacing: 0.5px;
  }
  .promise { position: absolute; left: 251px; top: 903px; white-space: nowrap; font-weight: 500; font-size: 17px; color: var(--black); }
</style>
</head>
<body>
<main class="flyer">
  <div class="hero-band"></div>
  <div class="dark-band"></div>
  <svg class="logo-blob" width="630" height="230" viewBox="0 0 630 230" aria-hidden="true">
    <path d="M0 0 H222 C248 40 248 140 172 165 C125 180 95 150 60 164 C30 177 10 205 0 216 Z" fill="#fff"/>
  </svg>

  <div class="brand"><span class="brand-dot"></span>Marvane Painting</div>

  <h1 class="headline"><span class="line-1">Upgrade Your</span><span class="line-2">Garage &amp; Driveway</span></h1>
  <p class="subhead">FROM WORN-OUT TO LIKE NEW</p>

  <div class="photo row-1 col-1 garage-before" role="img" aria-label="Bare, stained concrete garage floor before coating">
    <div class="tag before"><span>Before</span></div>
  </div>
  <div class="photo row-1 col-2 paver-before" role="img" aria-label="Faded paver driveway with landscaping before sealing">
    <div class="tag before"><span>Before</span></div>
  </div>
  <div class="photo row-2 col-1 garage-after" role="img" aria-label="Garage floor with glossy flake epoxy coating after">
    <div class="tag after"><span>After</span></div>
  </div>
  <div class="photo row-2 col-2 paver-after" role="img" aria-label="Sealed paver driveway with deep, rich color after">
    <div class="tag after"><span>After</span></div>
  </div>

  <section class="services">
    <div class="service epoxy">
      <h2 class="service-title">Epoxy Floor Coatings</h2>
      <ul class="benefits">
        <li><svg width="11" height="11" viewBox="0 0 12 12"><circle cx="6" cy="6" r="6" fill="#000"/><path d="M3.3 6.2 5.2 8 8.8 4.2" stroke="#fff" stroke-width="1.6" fill="none"/></svg>Durable, long-lasting finish</li>
        <li><svg width="11" height="11" viewBox="0 0 12 12"><circle cx="6" cy="6" r="6" fill="#000"/><path d="M3.3 6.2 5.2 8 8.8 4.2" stroke="#fff" stroke-width="1.6" fill="none"/></svg>Slip-resistant texture</li>
        <li><svg width="11" height="11" viewBox="0 0 12 12"><circle cx="6" cy="6" r="6" fill="#000"/><path d="M3.3 6.2 5.2 8 8.8 4.2" stroke="#fff" stroke-width="1.6" fill="none"/></svg>Covers cracks &amp;<br>imperfections</li>
        <li><svg width="11" height="11" viewBox="0 0 12 12"><circle cx="6" cy="6" r="6" fill="#000"/><path d="M3.3 6.2 5.2 8 8.8 4.2" stroke="#fff" stroke-width="1.6" fill="none"/></svg>Easy to clean &amp; maintain</li>
      </ul>
    </div>
    <div class="service sealing">
      <h2 class="service-title">Paver Sealing</h2>
      <ul class="benefits">
        <li><svg width="11" height="11" viewBox="0 0 12 12"><circle cx="6" cy="6" r="6" fill="#000"/><path d="M3.3 6.2 5.2 8 8.8 4.2" stroke="#fff" stroke-width="1.6" fill="none"/></svg>Restores color &amp; enhances<br>appearance</li>
        <li><svg width="11" height="11" viewBox="0 0 12 12"><circle cx="6" cy="6" r="6" fill="#000"/><path d="M3.3 6.2 5.2 8 8.8 4.2" stroke="#fff" stroke-width="1.6" fill="none"/></svg>Protects from sun fading</li>
        <li><svg width="11" height="11" viewBox="0 0 12 12"><circle cx="6" cy="6" r="6" fill="#000"/><path d="M3.3 6.2 5.2 8 8.8 4.2" stroke="#fff" stroke-width="1.6" fill="none"/></svg>Helps prevent weeds &amp; sand loss</li>
        <li><svg width="11" height="11" viewBox="0 0 12 12"><circle cx="6" cy="6" r="6" fill="#000"/><path d="M3.3 6.2 5.2 8 8.8 4.2" stroke="#fff" stroke-width="1.6" fill="none"/></svg>Easier to clean &amp; maintain</li>
      </ul>
    </div>
    <p class="tagline">Practical upgrades that protect and improve your home</p>
  </section>

  <div class="trust licensed">
    <svg class="trust-icon" viewBox="0 0 48 48" aria-hidden="true"><circle cx="24" cy="24" r="23" fill="#000" stroke="#3a8a3a" stroke-width="1.5"/><circle cx="24" cy="21" r="10" fill="none" stroke="#49a82a" stroke-width="3"/><path d="M19 21 23 25 30 17" stroke="#2488e2" stroke-width="3" fill="none"/><path d="M18 29 15 37 19 35 21 38 23 31M30 29 33 37 29 35 27 38 25 31" fill="#c0670c"/></svg>
    <p class="trust-text">Licensed &amp;<br>Insured</p>
  </div>
  <div class="trust family">
    <svg class="trust-icon" viewBox="0 0 48 48" aria-hidden="true"><circle cx="24" cy="24" r="23" fill="#000" stroke="#3a8a3a" stroke-width="1.5"/><path d="M22 11 32 14 V22 C32 29 27 33 22 35 C17 33 12 29 12 22 V14 Z" fill="#2e9c98"/><path d="M17 22 21 26 27 19" stroke="#000" stroke-width="2.2" fill="none"/><rect x="26" y="27" width="10" height="9" rx="2" fill="#c0670c"/></svg>
    <p class="trust-text">Family-Owned<br>Local Business</p>
  </div>
  <div class="trust area">
    <svg class="trust-icon" viewBox="0 0 48 48" aria-hidden="true"><circle cx="24" cy="24" r="23" fill="#000" stroke="#3a8a3a" stroke-width="1.5"/><ellipse cx="24" cy="34" rx="11" ry="4" fill="none" stroke="#c0670c" stroke-width="2"/><path d="M24 34 C20 28 16 24 16 19 A8 8 0 0 1 32 19 C32 24 28 28 24 34 Z" fill="#49a82a"/><circle cx="24" cy="19" r="3" fill="#2488e2"/></svg>
    <p class="trust-text">Serving Prescott &amp;<br>Surrounding Areas</p>
  </div>

  <p class="cta"><span class="small">CALL FOR A FREE</span><span class="big">ESTIMATE</span></p>
  <svg class="phone-icon" width="37" height="37" viewBox="0 0 37 37" aria-hidden="true">
    <defs><linearGradient id="phoneFill" x1="0" y1="0" x2="0" y2="1"><stop offset="0" stop-color="#2488e2"/><stop offset=".5" stop-color="#49a82a"/><stop offset="1" stop-color="#c0670c"/></linearGradient></defs>
    <circle cx="18.5" cy="18.5" r="18.5" fill="url(#phoneFill)"/>
    <path d="M12 10 C10 12 10 16 14 21 C18 26 23 28 26 26 L27 24 23 21 21 23 C19 22 16 19 15 17 L17 15 14 11 Z" fill="#fff"/>
  </svg>
  <p class="phone-number">928-555-0147</p>
  <p class="promise">Fast, professional service you can trust</p>
</main>
</body>
</html>
```